Diverse, up-scale salon needs eye-catching, unique business cards.

We are looking for a unique business card design for our stylist but that can also be multi functional and used for appointment reminder and referrals. I will need a design in a format that I can modify names and titles going forward. In the past we have had a dark background with the logo on one side, and stylist and contact information on the other but we are open to all ideas. I have included our mission statement as well as branded colors below. The statement doesn't need to go on the card, it's just a reference for target market. We need space for the stylists name, title, instagram handle and then the salons phone number, website and address. I am also open to adding a spot for a qr code linked to the stylist instagram or the salon booking link.

primary brand colors:
#333333 #233415 #36502a #93874a #000000
Mission statement:
Morvane Hair Studio, a high-end salon located in the lively Downtown Farmington, Michigan, is committed to providing exceptional services in a welcoming and relaxed environment to meet the needs of our diverse clientele.
Our salon specializes in contemporary custom haircuts, coloring, extensions, and barbering and beard grooming services. Our team of skilled stylists is passionate and inventive in their hair styling techniques. At the heart of our salon are values centered on quality, innovation, creativity, and above all, comfort. These core values are evident in every appointment across our customizable array of services.
Our goal is to establish a benchmark for exceptional hair care for every human.
Website: www.morvanehairstudio-demo.com
instagram: @morvanehairstudio
address: 41872 Pelton Brook Rd, Linden Vale OH
phone: 555-316-8847

Industry/Entity Type

Hair Salon

Contact Information for Business Card

Stylist name, title, phone, instagram, website, address, (optional qr code)

Requirements
Should not have
• Does not need mission statement on the card.

```html
<!DOCTYPE html>
<html lang="en">
<head>
<meta charset="utf-8">
<title>Morvane Hair Studio — Business Card</title>
<link rel="stylesheet" href="https://fonts.googleapis.com/css2?family=Josefin+Sans:wght@400;600&family=Plus+Jakarta+Sans:wght@400;500&display=swap">
<style>
  :root {
    --backdrop: #554f3d;
    --card: #ffffff;
    --gold: #93874a;
    --ink: #333333;
    --faint: #f2f2f2;
  }
  * { margin: 0; padding: 0; box-sizing: border-box; }
  html, body { width: 676px; height: 1200px; overflow: hidden; }
  body {
    background: var(--backdrop);
    font-family: "Plus Jakarta Sans", Arial, sans-serif;
    position: relative;
  }
  .card {
    position: absolute;
    left: 102px;
    width: 472px;
    height: 270px;
    background: var(--card);
    overflow: hidden;
    box-shadow: 0 4px 10px rgba(0,0,0,0.35);
  }
  .card--front { top: 305px; }
  .card--back { top: 624px; }
  .card__ring {
    position: absolute;
    width: 230px;
    height: 230px;
    border: 9px solid var(--faint);
    border-radius: 50%;
    right: -80px;
    top: 20px;
  }
  .brand-name {
    position: absolute;
    font-family: "Josefin Sans", Arial, sans-serif;
    font-weight: 600;
    color: var(--gold);
    text-transform: uppercase;
    text-align: center;
    line-height: 1.1;
    letter-spacing: 0.12em;
  }
  .card--front .brand-name {
    left: 0;
    right: 0;
    top: 106px;
    font-size: 26px;
  }
  .card--back .brand-name {
    left: 22px;
    width: 200px;
    top: 112px;
    font-size: 21px;
  }
  .brand-name small { display: block; font-size: 0.55em; letter-spacing: 0.3em; margin-top: 6px; }
  .stylist {
    position: absolute;
    left: 244px;
    top: 58px;
  }
  .stylist__name {
    font-family: "Josefin Sans", Arial, sans-serif;
    font-weight: 600;
    font-size: 17px;
    letter-spacing: 0.06em;
    color: var(--gold);
    text-transform: uppercase;
  }
  .stylist__title {
    font-family: "Josefin Sans", Arial, sans-serif;
    font-size: 11px;
    letter-spacing: 0.14em;
    color: var(--ink);
    text-transform: uppercase;
    margin-top: 2px;
  }
  .contact { list-style: none; margin-top: 14px; }
  .contact__item {
    display: flex;
    align-items: flex-start;
    gap: 10px;
    font-size: 11.5px;
    color: var(--ink);
    line-height: 1.25;
    margin-bottom: 9px;
  }
  .contact__icon { width: 14px; height: 14px; flex: none; }
</style>
</head>
<body>
  <section class="card card--front">
    <div class="card__ring"></div>
    <div class="brand-name">Morvane<small>Hair Studio</small></div>
  </section>

  <section class="card card--back">
    <div class="card__ring"></div>
    <div class="brand-name">Morvane<small>Hair Studio</small></div>
    <div class="stylist">
      <h1 class="stylist__name">Dana Whitlow</h1>
      <p class="stylist__title">CEO, Founder</p>
      <ul class="contact">
        <li class="contact__item">
          <svg class="contact__icon" viewBox="0 0 24 24" fill="none" stroke="#93874a" stroke-width="1.6"><path d="M5 3h4l2 5-2.5 1.5a11 11 0 0 0 6 6L16 13l5 2v4a2 2 0 0 1-2 2A17 17 0 0 1 3 5a2 2 0 0 1 2-2z"/></svg>
          <span>555-316-8847</span>
        </li>
        <li class="contact__item">
          <svg class="contact__icon" viewBox="0 0 24 24" fill="none" stroke="#93874a" stroke-width="1.6"><path d="M12 21s-6-6.2-6-11a6 6 0 0 1 12 0c0 4.8-6 11-6 11z"/><circle cx="12" cy="10" r="2.3"/></svg>
          <span>41872 Pelton Brook Rd,<br>Linden Vale OH</span>
        </li>
        <li class="contact__item">
          <svg class="contact__icon" viewBox="0 0 24 24" fill="none" stroke="#93874a" stroke-width="1.6"><circle cx="12" cy="12" r="9"/><path d="M3 12h18M12 3c3 3 3 15 0 18M12 3c-3 3-3 15 0 18"/></svg>
          <span>www.morvanehairstudio-demo.com</span>
        </li>
        <li class="contact__item">
          <svg class="contact__icon" viewBox="0 0 24 24" fill="none" stroke="#93874a" stroke-width="1.6"><rect x="3" y="3" width="18" height="18" rx="3"/></svg>
          <span>@morvanehairstudio</span>
        </li>
      </ul>
    </div>
  </section>
</body>
</html>
```